Existing Website Requiring new Pages

I have an existing word press website that was built using elementor.
Website: www.tallowmerecare.com.au
I require the Vacancies page (https://www.tallowmerecare.com.au/vacancies/) to be modified to display our new properties along with minor tweaks to how the information is presented.
The vacancies to be displayed are the exactly the same as those that are located on the homepage of QDA website (https://qda.org.au/)
The new pages that link off the Vacancies tab will require custom design.
There are roughly 8 pages/properties to be incorporated. i wish for the design to be very similar to that displayed in the following link; https://www.zomplex.com.au/vacancies/merrylands
Along with this the back end has not been updated for the last 3 years so it also requires some maintenance.
Website is in the disability industry and the custom pages will display information relative to Property Vacancies.
I have attached a ZIP file with some design guides, the information for each of the properties (which will need to be modified to show our business name Tallowmere Healthcare) and the example of how it is to look based off the Zomplex website.
If you guys have any suggestions or ideas on how to make this more presentable or possible i'm open to your ideas.
People looking for SDA properties custom built for people with a disability
Disability
Coded - Design and coding required
5+ page

```html
<!DOCTYPE html>
<html lang="en">
<head>
<meta charset="utf-8">
<title>Vacancies – Tallowmere Healthcare</title>
<link href="https://fonts.googleapis.com/css2?family=Open+Sans:wght@400;600;700&family=Oswald:wght@400;500&display=swap" rel="stylesheet">
<style>
:root{
  --ink:#1d1d1f;
  --muted:#555a60;
  --pink:#f2478f;
  --pink-deep:#ee2f7a;
  --orange:#ec6b3a;
  --teal:#2bb7b3;
  --white:#ffffff;
  --card-shadow:0 2px 8px rgba(0,0,0,.22);
}
*{box-sizing:border-box;margin:0;padding:0}
html,body{width:924px;height:1200px;overflow:hidden;background:var(--white)}
body{position:relative;font-family:"Open Sans",sans-serif;color:var(--ink)}

.site-header{position:absolute;top:0;left:0;width:924px;height:69px;background:var(--white);z-index:3}
.brand-tab{position:absolute;left:66px;top:0;width:172px;height:108px;z-index:4}
.brand-tab svg{position:absolute;inset:0}
.brand-name{position:absolute;left:20px;top:62px;width:132px;text-align:center;font-family:"Oswald",sans-serif;font-weight:400;font-size:15px;line-height:1.1;color:var(--ink);letter-spacing:.3px}
.brand-dot{position:absolute;left:74px;top:24px;width:26px;height:26px;border-radius:50%;background:var(--pink)}
.main-nav{position:absolute;top:26px;left:324px;display:flex;gap:25px;font-weight:700;font-size:11px;letter-spacing:.1px}
.main-nav a{color:var(--ink);text-decoration:none}
.main-nav .current{color:var(--orange);border-bottom:1px solid var(--orange)}
.contact-btn{position:absolute;left:729px;top:16px;width:118px;height:35px;border-radius:18px;background:linear-gradient(90deg,#f25a9b,var(--pink-deep));color:var(--white);font-weight:700;font-size:11px;display:flex;align-items:center;justify-content:center}

.hero{position:absolute;top:69px;left:0;width:924px;height:373px;overflow:hidden}
.hero-backdrop{position:absolute;inset:0;background:
  radial-gradient(ellipse 260px 160px at 620px 180px,rgba(243,88,150,.95),transparent 70%),
  radial-gradient(ellipse 200px 140px at 860px 120px,rgba(64,190,200,.85),transparent 70%),
  radial-gradient(ellipse 260px 140px at 860px 330px,rgba(245,200,110,.95),transparent 70%),
  linear-gradient(90deg,#ece9e6 0%,#e4dfdb 45%,#f3a9c6 70%,#d7b9d6 100%)}
.hero-photo{position:absolute;left:0;top:0;width:470px;height:373px;background:linear-gradient(90deg,#e8e1d3 0%,#ece8e4 55%,rgba(236,232,228,0) 100%)}
.hero-title{position:absolute;left:496px;top:124px;font-family:"Oswald",sans-serif;font-weight:400;font-size:72px;line-height:1;color:var(--white);letter-spacing:-.5px}
.hero-wave{position:absolute;left:0;bottom:0;width:924px;height:120px}

.vacancy-grid{position:absolute;left:85px;top:502px;display:grid;grid-template-columns:repeat(4,176px);column-gap:17px;row-gap:30px}
.vacancy-card{position:relative;width:176px;height:206px;background:var(--white);padding:3px;box-shadow:var(--card-shadow);border-radius:3px}
.vacancy-photo{width:100%;height:100%;border-radius:2px}
.vacancy-label{position:absolute;left:10px;top:141px;width:156px;height:53px;background:var(--white);border-radius:3px;box-shadow:0 1px 4px rgba(0,0,0,.15);text-align:center;padding-top:10px}
.vacancy-label h3{font-weight:700;font-size:12px;letter-spacing:.2px}
.vacancy-label p{font-size:9.5px;color:var(--muted);margin-top:5px}
.tone-a{background:linear-gradient(#e9edf2 0%,#dfe3e8 55%,#6f7a62 80%,#8c8a84 100%)}
.tone-b{background:linear-gradient(#a9d0ee 0%,#b87a5f 35%,#5f8a3a 60%,#c98f72 100%)}
.tone-c{background:linear-gradient(#6fb3e4 0%,#9fcbee 40%,#e8dcc0 70%,#5d8c47 100%)}
.tone-d{background:linear-gradient(#7ab6e2 0%,#e6d8c8 45%,#cbbdaa 75%,#6d8a4f 100%)}
.tone-e{background:linear-gradient(#5ea9e0 0%,#9fcbe9 35%,#c59a72 65%,#4f9a38 100%)}
.tone-f{background:linear-gradient(#6fb1e8 0%,#c9e0f2 35%,#d87a4a 62%,#6ab04a 100%)}
.tone-g{background:linear-gradient(#4e8a3a 0%,#d5625c 35%,#d8cbb6 60%,#6a7356 100%)}
.tone-h{background:linear-gradient(#e9a0a8 0%,#c7b8b4 35%,#6e6a64 65%,#4d6a3c 100%)}

.footer-bg{position:absolute;left:0;top:870px;width:924px;height:330px;background:linear-gradient(90deg,#fde3ee 0%,#fdf0e2 40%,#f4f6dc 70%,#e2f7f1 100%)}
.footer-wave{position:absolute;left:0;top:870px;width:924px;height:120px}
.footer-brand{position:absolute;left:86px;top:1020px;width:92px}
.footer-brand .brand-dot{position:static;display:block;margin:0 auto 8px;width:30px;height:30px}
.footer-brand span{display:block;text-align:center;font-family:"Oswald",sans-serif;font-size:15px;line-height:1.1;color:var(--ink)}
.footer-col{position:absolute;top:1027px}
.footer-col h4{font-weight:400;font-size:12.5px;letter-spacing:.2px;margin-bottom:12px;color:var(--ink)}
.footer-col li{list-style:none;font-size:11px;color:var(--muted);line-height:20.5px}
.col-contact{left:232px}
.col-accom{left:469px}
.col-services{left:707px}
.contact-row{display:flex;align-items:center;gap:10px;font-size:11.5px;color:var(--muted);line-height:23px}
.contact-row svg{width:12px;height:12px;fill:#555a60}
.social{position:absolute;left:227px;top:1103px;display:flex;gap:4px}
.social span{width:26px;height:26px;border-radius:50%;background:var(--white);box-shadow:0 1px 3px rgba(0,0,0,.15)}
.social span:first-child{background:var(--pink-deep)}
.copyright{position:absolute;left:0;top:1166px;width:936px;text-align:center;font-size:9.5px;color:var(--ink)}
</style>
</head>
<body>

<header class="site-header">
  <nav class="main-nav">
    <a href="#">HOME</a>
    <a href="#">ABOUT US</a>
    <a href="#" class="current">WHAT WE DO ▾</a>
    <a href="#">REFERRALS</a>
    <a href="#">FEEDBACK</a>
  </nav>
  <div class="contact-btn">CONTACT US</div>
</header>

<div class="brand-tab">
  <svg viewBox="0 0 172 108" width="172" height="108"><path d="M0 69 L172 69 L172 69 L152 100 Q148 108 138 108 L34 108 Q24 108 20 100 Z" fill="#fff"/><rect x="0" y="0" width="172" height="69" fill="#fff"/></svg>
  <span class="brand-dot"></span>
  <div class="brand-name">Tallowmere Healthcare</div>
</div>

<section class="hero">
  <div class="hero-backdrop"></div>
  <div class="hero-photo" role="img" aria-label="Photo of a woman in a wheelchair in a bright living room"></div>
  <h1 class="hero-title">VACANCIES</h1>
  <svg class="hero-wave" viewBox="0 0 924 120" preserveAspectRatio="none">
    <path d="M0 25 C60 0 130 10 190 45 C260 85 330 100 420 70 C500 45 560 10 640 35 C720 60 790 40 860 20 C890 12 910 14 924 20 L924 120 L0 120 Z" fill="#fff" opacity=".55"/>
    <path d="M0 35 C70 10 140 25 200 65 C270 110 350 115 430 85 C510 55 570 25 650 50 C730 75 800 60 870 35 C895 27 912 28 924 32 L924 120 L0 120 Z" fill="#fff"/>
  </svg>
</section>

<div class="footer-bg"></div>
<svg class="footer-wave" viewBox="0 0 924 120" preserveAspectRatio="none">
  <path d="M0 0 L924 0 L924 80 C860 60 780 70 700 90 C620 110 540 112 470 100 C400 88 330 70 250 82 C170 94 90 90 0 70 Z" fill="#fff"/>
</svg>

<main class="vacancy-grid">
  <article class="vacancy-card"><div class="vacancy-photo tone-a" role="img" aria-label="Photo of the Penrith house"></div><div class="vacancy-label"><h3>PENRITH</h3><p>4 BEDROOM SIL HOME</p></div></article>
  <article class="vacancy-card"><div class="vacancy-photo tone-b" role="img" aria-label="Photo of the Mount Druitt house"></div><div class="vacancy-label"><h3>MOUNT DRUITT</h3><p>4 BEDROOM SIL HOME</p></div></article>
  <article class="vacancy-card"><div class="vacancy-photo tone-c" role="img" aria-label="Photo of the Casula house"></div><div class="vacancy-label"><h3>CASULA</h3><p>4 BEDROOM SIL HOME</p></div></article>
  <article class="vacancy-card"><div class="vacancy-photo tone-d" role="img" aria-label="Photo of the Eastwood house"></div><div class="vacancy-label"><h3>EASTWOOD</h3><p>4 BEDROOM SIL HOME</p></div></article>
  <article class="vacancy-card"><div class="vacancy-photo tone-e" role="img" aria-label="Photo of the Baulkham Hills house"></div><div class="vacancy-label"><h3>BAULKHAM HILLS</h3><p>4 BEDROOM SIL HOME</p></div></article>
  <article class="vacancy-card"><div class="vacancy-photo tone-f" role="img" aria-label="Photo of the Merrylands house"></div><div class="vacancy-label"><h3>MERRYLANDS</h3><p>4 BEDROOM SIL HOME</p></div></article>
  <article class="vacancy-card"><div class="vacancy-photo tone-g" role="img" aria-label="Photo of the Luna Park house"></div><div class="vacancy-label"><h3>LUNA PARK</h3><p>4 BEDROOM SIL HOME</p></div></article>
  <article class="vacancy-card"><div class="vacancy-photo tone-h" role="img" aria-label="Photo of the Bondi Beach house"></div><div class="vacancy-label"><h3>BONDI BEACH</h3><p>4 BEDROOM SIL HOME</p></div></article>
</main>

<footer>
  <div class="footer-brand"><span class="brand-dot"></span><span>Tallowmere Healthcare</span></div>

  <div class="footer-col col-contact">
    <h4>CONTACT US</h4>
    <div class="contact-row"><svg viewBox="0 0 12 12"><path d="M0 2h12v8H0z M0 2l6 4 6-4" fill="#555a60"/><path d="M0.8 2.6 6 6 11.2 2.6" stroke="#fdf0e6" stroke-width="1" fill="none"/></svg>info@tallowmerecare.com.au</div>
    <div class="contact-row"><svg viewBox="0 0 12 12"><path d="M2.5 0.5 4.5 3 3.3 4.4C4 6 6 8 7.6 8.7L9 7.5 11.5 9.5 10 11.5C5.5 11 1 6.5 0.5 2Z"/></svg>+61 0491 570 156</div>
  </div>
  <div class="social"><span></span><span></span><span></span></div>

  <div class="footer-col col-accom">
    <h4>ACCOMMODATION</h4>
    <ul>
      <li>Supported Independent Living (SIL)</li>
      <li>Specialist Disability Accommodation (SDA)</li>
      <li>Short term Accommodation (Respite)</li>
      <li>Vacancies</li>
    </ul>
  </div>

  <div class="footer-col col-services">
    <h4>WHAT WE DO</h4>
    <ul>
      <li>In Home Care</li>
      <li>Social &amp; Community Services</li>
      <li>Therapeutic Supports</li>
      <li>Support Coordination</li>
      <li>Home Modifications</li>
    </ul>
  </div>

  <p class="copyright">© Copyright 2024 | Tallowmere Healthcare | All Rights Reserved.</p>
</footer>

</body>
</html>
```